Tamburetti, the Postcard Café is looking for new postcards.

Tamburetti sells loads of cards and is always looking for new designs. After three years of selling cards produced by others we are now ready to start our own collection.

What is Tamburetti?
Tamburetti is a place where you, while drinking coffee or tea, can choose a postcard (we have 300 to 400 different kinds for you to choose from), write it, and have it send on any day you want. We are located in the beautiful city of Leiden, The Netherlands. See enclosed document for more info.

What are we looking for?
Funny, witty, colorful designs that make people smile or think. We are thinking to start out with at least 10 different designs.

The dimensions of the cards are 10 x 14,8 cm, either landscape or portrait. Please enter your design in both pdf and original format (ai. psd. or id. file) where possible in vector.

Designs that are offensive to whatever group of people will be removed immediately.

What's in it for you?
You will become part of the Tamburetti collection which you can prove because your name will be on the back of the card.
Furthermore we will pay you € 125,- per chosen postcard.

```html
<!DOCTYPE html>
<html lang="en">
<head>
<meta charset="utf-8">
<title>Summer Please — Postcard</title>
<link rel="stylesheet" href="https://fonts.googleapis.com/css2?family=Indie+Flower&display=swap">
<style>
  :root {
    --sky-teal: #3fd0b4;
    --sky-mint: #9fe3cf;
    --sky-pale: #dcefe3;
    --sun-cream: #f6ecc4;
    --sun-gold: #f3b65a;
    --sun-ember: #b4380f;
    --field-dark: #120606;
    --ribbon: #45c19c;
    --ribbon-fold: #2f5b4d;
    --ink: #0b0b0b;
  }
  html, body {
    margin: 0;
    padding: 0;
    width: 1200px;
    height: 811px;
    overflow: hidden;
    background: #ffffff;
  }
  .postcard {
    position: relative;
    width: 1200px;
    height: 811px;
    overflow: hidden;
  }
  .sunset-photo {
    position: absolute;
    inset: 0;
    background: linear-gradient(90deg,
      var(--sky-teal) 0%,
      var(--sky-mint) 28%,
      var(--sky-pale) 44%,
      var(--sun-cream) 53%,
      var(--sun-gold) 56.5%,
      var(--sun-ember) 58.2%,
      var(--field-dark) 60%,
      #050202 100%);
  }
  .ribbons {
    position: absolute;
    inset: 0;
  }
  .ribbon-band { fill: var(--ribbon); opacity: 0.96; }
  .ribbon-fold { fill: var(--ribbon-fold); }
  .ribbon-word {
    font-family: "Indie Flower", cursive;
    font-size: 170px;
    font-weight: 400;
    fill: var(--ink);
  }
</style>
</head>
<body>
  <main class="postcard">
    <div class="sunset-photo" role="img" aria-label="Photograph of a sunset over a dark grass field, sky fading from teal to golden light, seen sideways with grass stalks against the glow"></div>

    <svg class="ribbons" width="1200" height="811" viewBox="0 0 1200 811">
      <g class="ribbon ribbon--summer">
        <polygon class="ribbon-band" points="355,673 462,673 462,793 408,760 355,793"/>
        <polygon class="ribbon-fold" points="355,673 403,673 403,713"/>
        <polygon class="ribbon-band" points="403,205 455,222 508,192 508,714 403,714"/>
      </g>
      <g class="ribbon ribbon--please">
        <polygon class="ribbon-band" points="605,16 658,49 712,16 712,136 605,136"/>
        <polygon class="ribbon-fold" points="667,99 712,136 667,136"/>
        <polygon class="ribbon-band" points="559,99 667,99 667,618 613,600 559,618"/>
      </g>

      <text class="ribbon-word ribbon-word--summer" x="487" y="662"
            transform="rotate(-90 487 662)"
            textLength="505" lengthAdjust="spacingAndGlyphs">summer</text>
      <text class="ribbon-word ribbon-word--please" x="667" y="598"
            transform="rotate(-90 667 598)"
            textLength="380" lengthAdjust="spacingAndGlyphs">please</text>
    </svg>
  </main>
</body>
</html>
```